The Brindlewick Project

All information regarding the design is located at Brindlewick.com. Any questions regarding the project, will be answered on the site.

```html
<!DOCTYPE html>
<html lang="en">
<head>
<meta charset="utf-8">
<title>Brindlewick</title>
<link rel="stylesheet" href="https://fonts.googleapis.com/css2?family=PT+Sans:wght@400;700&display=swap">
<style>
  :root {
    --brand-blue: #0a8fbf;
    --brand-blue-dark: #056f9a;
    --accent-green: #8cbf1f;
    --tab-bar: #f7f7f7;
    --tab-active: #e6e6e6;
    --tab-text: #555555;
    --text-dark: #333333;
    --placeholder: #777777;
    --footer-bg: #9a9a9a;
    --white: #ffffff;
    --bg-light: #f4f4f4;
    --bg-edge: #d9d9d9;
  }
  * { box-sizing: border-box; margin: 0; padding: 0; }
  html, body { width: 1200px; height: 940px; overflow: hidden; }
  body {
    position: relative;
    font-family: Arial, Helvetica, sans-serif;
    background: radial-gradient(ellipse 700px 520px at 600px 430px, var(--bg-light) 0%, var(--bg-edge) 100%);
  }
  .tab-bar {
    position: absolute; left: 0; top: 0; width: 1200px; height: 50px;
    background: var(--tab-bar);
    border-bottom: 1px solid #e2e2e2;
  }
  .tab {
    position: absolute; top: 0; height: 49px; line-height: 47px;
    font-size: 17px; color: var(--tab-text); text-decoration: none;
    transform: translateX(-50%); white-space: nowrap;
  }
  .tab.is-active {
    left: 0; width: 100px; transform: none; text-align: center;
    background: var(--tab-active); color: #222;
  }
  .login-link {
    position: absolute; right: 17px; top: 71px;
    font-size: 17px; color: #222; text-decoration: none;
  }
  .brand {
    position: absolute; left: 0; top: 300px; width: 1200px;
    text-align: center;
    font-family: "PT Sans", sans-serif; font-weight: 700;
    font-size: 96px; color: var(--brand-blue); line-height: 1;
  }
  .brand-mark {
    display: inline-block; width: 34px; height: 34px; border-radius: 50%;
    background: var(--brand-blue); margin-right: 20px; vertical-align: 10px;
  }
  .search-box {
    position: absolute; left: 189px; top: 440px; width: 858px; height: 68px;
    border-radius: 34px; background: #fcfcfc;
    border: 1px solid #d4d4d4;
    box-shadow: inset 0 2px 3px rgba(0,0,0,0.06);
  }
  .search-input {
    position: absolute; left: 28px; top: 0; height: 66px; line-height: 66px;
    font-family: "PT Sans", sans-serif; font-size: 21px; color: var(--placeholder);
  }
  .search-button {
    position: absolute; right: 16px; top: 10px; width: 104px; height: 47px;
    border-radius: 20px; border: none;
    background: linear-gradient(#1aa0cc, var(--brand-blue-dark));
    color: var(--white); font-family: "PT Sans", sans-serif; font-weight: 700;
    font-size: 22px; letter-spacing: 0.5px;
  }
  .ad-count {
    position: absolute; left: 0; top: 536px; width: 1200px; text-align: center;
    font-size: 20px; color: var(--text-dark);
  }
  .ad-count strong { color: var(--accent-green); }
  .site-footer {
    position: absolute; left: 0; top: 890px; width: 1200px; height: 50px;
    background: var(--footer-bg);
    font-size: 14.5px; color: var(--white); text-align: right;
    padding-right: 16px; line-height: 52px;
  }
  .site-footer a { color: var(--white); text-decoration: none; }
</style>
</head>
<body>
  <nav class="tab-bar">
    <a class="tab is-active" href="#">List</a>
    <a class="tab" style="left:179px" href="#">Step by step</a>
    <a class="tab" style="left:323px" href="#">Image</a>
    <a class="tab" style="left:426px" href="#">Link</a>
    <a class="tab" style="left:521px" href="#">Text</a>
    <a class="tab" style="left:663px" href="#">Video(Streamly)</a>
  </nav>

  <a class="login-link" href="#">Brindlewick - Login Now</a>

  <h1 class="brand"><span class="brand-mark"></span>Brindlewick</h1>

  <form class="search-box">
    <span class="search-input">Write your question here</span>
    <button class="search-button" type="button">Search</button>
  </form>

  <p class="ad-count"><strong>40,217</strong> updated real estate classified ads</p>

  <footer class="site-footer">
    © 2010 Copyright | <a href="#">About</a> &nbsp;| <a href="#">Privacy</a> | <a href="#">Legal</a> | <a href="#">Help</a> | <a href="#">Feedback</a>
  </footer>
</body>
</html>
```